Electronic Time-sheet & Training Tracker for Mobile phone

App should have two functions:Access by Quillon and Vextora:Employee Tracker: I need to be able to add/edit employees and personal information (example: address, DL number, SS number, DOB, employee number), drug screen information (type DCCHA and expiration date, DCCFO and expiration date, DCCHT and expiration date, PRAV Background and expiration date) and enter multiple training records (KEMB8 and expiration date). It would be great to receive an expiration alert.The employee would only have visibility to his own. Supervisors would have overall visibility.Time-Sheet:I need a time-sheet that can be accessed on the phone, be completed, then have the ability to electronically sign and submitted. The timesheet needs to be used two-fold for supervision to verify hours and edit (if need be), he would approve and forward to payroll. The time-sheet should be daily or weekly if we can get the data to fit. We are trying to streamline field supervisors having to log on to a computer to access a server just to do time-sheets. We need it to be user-friendly. We need to have two places to have electronic signatures (employee and supervisor).
A couple of designers have asked for an additional day. Others are making changes based on feedback.
Industrial (Oil ad Gas)
- Timesheet portion may require multiple entries with billable, non-billable, shop drop-down and job number and category code (LRS, HTS, FMS, ITP, OBS, HTT, NDE)
- Tracker - Training expiration alert or notifications by email to employee and supervisors.

```html
<!DOCTYPE html>
<html lang="en">
<head>
<meta charset="utf-8">
<title>Shift Overview – Time-sheet & Training Tracker</title>
<link rel="stylesheet" href="https://fonts.googleapis.com/css2?family=Hind:wght@300;400;500;600;700&display=swap">
<style>
  :root {
    --page-bg: #eceef3;
    --screen-bg: #ffffff;
    --ink: #1d1d1f;
    --ink-soft: #3a3a3c;
    --muted: #6b6b70;
    --navy: #24338a;
    --card-border: #efc3c0;
    --pill-fill: #f1c8c1;
    --pill-border: #8c6d6a;
    --btn-start: #5468e2;
    --btn-end: #9eabf6;
    --alert-red: #e5322d;
    --bell: #f2b21b;
    --ring-dark: #222226;
    --ring-blue-a: #24338a;
    --ring-blue-b: #5b7cf0;
    --ring-purple: #9b5de5;
    --ring-cyan: #3aa7f0;
    --accent: #e8663a;
    --nav-bg: #f6f6f8;
    --divider: #e6e6ea;
  }
  * { box-sizing: border-box; margin: 0; padding: 0; }
  html, body {
    width: 1200px; height: 2400px; overflow: hidden;
    background: var(--page-bg);
    font-family: "Hind", sans-serif;
    color: var(--ink);
  }
  .screen {
    position: absolute; left: 47px; top: 5px;
    width: 375px; height: 810px;
    background: var(--screen-bg);
    transform: scale(2.95); transform-origin: top left;
    overflow: hidden;
  }
  .abs { position: absolute; }

  /* status bar */
  .status-time { left: 29px; top: 14px; font-size: 14px; font-weight: 500; color: #8a8a8e; }
  .status-icons { right: 24px; top: 16px; }

  /* header */
  .menu-toggle { left: 18px; top: 73px; }
  .greeting { right: 60px; top: 62px; text-align: right; line-height: 1; }
  .greeting-hello { font-size: 15px; font-weight: 500; }
  .greeting-name { font-size: 25px; font-weight: 500; margin-top: 6px; }
  .avatar {
    right: 12px; top: 62px; width: 48px; height: 48px; border-radius: 50%;
    background: radial-gradient(circle at 50% 40%, #c9a48c, #6c4f3f 70%, #3a2f2a);
    border: 2px solid #fff; box-shadow: 0 1px 4px rgba(0,0,0,.25);
  }

  /* shift card */
  .shift-card {
    left: 13px; top: 137px; width: 350px; height: 258px;
    border: 1px solid var(--card-border); border-radius: 6px;
    box-shadow: 0 2px 8px rgba(0,0,0,.08);
  }
  .shift-date { left: 14px; top: 12px; font-size: 11px; color: var(--ink-soft); }
  .shift-countdown { left: 14px; top: 34px; display: flex; align-items: baseline; }
  .shift-label { font-size: 17px; line-height: 17px; font-weight: 400; }
  .shift-value { font-size: 38px; font-weight: 400; margin-left: 7px; line-height: 1; }
  .shift-unit { font-size: 23px; margin-right: 14px; }
  .pill {
    top: 99px; height: 25px; border-radius: 13px;
    background: var(--pill-fill); border: 1px solid var(--pill-border);
    font-size: 11px; font-weight: 600; display: flex; align-items: center;
    padding-top: 2px;
  }
  .pill-billing { left: 11px; width: 97px; justify-content: center; }
  .pill-location { left: 120px; width: 218px; padding-left: 24px; justify-content: space-between; padding-right: 10px; }
  .shift-meta { top: 155px; font-size: 13px; color: var(--navy); }
  .shift-meta strong { font-weight: 700; }
  .meta-job { left: 11px; }
  .meta-category { right: 11px; }
  .btn-primary {
    display: flex; align-items: center; justify-content: center;
    color: #fff; font-size: 14px; font-weight: 500; padding-top: 2px;
    background: linear-gradient(90deg, var(--btn-start), var(--btn-end));
    border-radius: 6px; box-shadow: 0 5px 10px rgba(84,104,226,.3);
  }
  .btn-clock-in { left: 100px; top: 202px; width: 130px; height: 37px; }

  /* alert */
  .alert-card {
    left: 13px; top: 416px; width: 350px; height: 59px;
    border: 1px solid #efeff2; border-radius: 4px; box-shadow: 0 1px 4px rgba(0,0,0,.05);
  }
  .alert-bell { left: 17px; top: 16px; }
  .alert-text { left: 72px; top: 21px; font-size: 14px; font-weight: 600; }
  .alert-text .days { color: var(--alert-red); }
  .alert-close { right: 10px; top: 16px; font-size: 15px; color: #b8b8bd; }

  /* weekly report */
  .section-title { left: 11px; top: 497px; font-size: 20px; font-weight: 400; }
  .report-card {
    left: 11px; top: 526px; width: 350px; height: 199px;
    border-radius: 5px; box-shadow: 0 1px 8px rgba(0,0,0,.1);
  }
  .metric { top: 18px; width: 100px; text-align: center; }
  .metric-work { left: 4px; }
  .metric-leave { left: 121px; }
  .metric-training { left: 237px; }
  .metric-label { font-size: 10px; font-weight: 600; }
  .metric-ring { position: relative; width: 70px; height: 70px; margin: 10px auto 0; }
  .metric-ring span {
    position: absolute; inset: 0; display: flex; align-items: center; justify-content: center;
    font-size: 15px; font-weight: 700; padding-top: 3px;
  }
  .metric-hours { font-size: 9px; color: var(--ink-soft); margin-top: 3px; }
  .btn-approve { left: 69px; top: 152px; width: 211px; height: 36px; font-weight: 400; }

  /* bottom nav */
  .tab-bar {
    left: 0; top: 738px; width: 375px; height: 72px;
    background: var(--nav-bg); border-top: 1px solid var(--divider);
    display: flex; justify-content: space-around; padding: 14px 6px 0;
  }
  .tab { width: 80px; text-align: center; font-size: 11px; color: var(--ink-soft); }
  .tab svg { display: block; margin: 0 auto 5px; }
  .tab-active { color: var(--accent); }
</style>
</head>
<body>
<main class="screen">
  <div class="abs status-time">9:41</div>
  <svg class="abs status-icons" width="56" height="12" viewBox="0 0 56 12" aria-hidden="true">
    <g fill="#8a8a8e">
      <rect x="0" y="8" width="3" height="4" rx="1"/><rect x="4.5" y="6" width="3" height="6" rx="1"/>
      <rect x="9" y="3.5" width="3" height="8.5" rx="1"/><rect x="13.5" y="1" width="3" height="11" rx="1"/>
      <path d="M27 11.5l-2.2-2.4a3.2 3.2 0 014.4 0z"/>
      <path d="M22.6 6.8a6.4 6.4 0 018.8 0l-1.3 1.3a4.6 4.6 0 00-6.2 0z"/>
      <path d="M20.4 4.5a9.6 9.6 0 0113.2 0l-1.3 1.3a7.8 7.8 0 00-10.6 0z"/>
      <rect x="40" y="2" width="19" height="9" rx="2.5" fill="none" stroke="#8a8a8e" transform="translate(-4 0)"/>
      <rect x="38" y="4" width="14" height="5" rx="1"/>
    </g>
  </svg>

  <svg class="abs menu-toggle" width="28" height="22" viewBox="0 0 28 22" aria-label="Menu">
    <g stroke="#555" stroke-width="2.5" stroke-linecap="round">
      <line x1="2" y1="3" x2="26" y2="3"/><line x1="2" y1="11" x2="26" y2="11"/><line x1="2" y1="19" x2="26" y2="19"/>
    </g>
  </svg>
  <div class="abs greeting">
    <p class="greeting-hello">Good day!,</p>
    <p class="greeting-name">Dorian.</p>
  </div>
  <div class="abs avatar" role="img" aria-label="Profile photo of the employee"></div>

  <section class="abs shift-card">
    <p class="abs shift-date">Wednesday 4th Feb 2019, 18:24:45</p>
    <div class="abs shift-countdown">
      <p class="shift-label">Your next<br>shift starts in</p>
      <p class="shift-value">6<span class="shift-unit">min</span>15<span class="shift-unit">sec</span></p>
    </div>
    <div class="abs pill pill-billing">BILLABLE</div>
    <div class="abs pill pill-location">SHOP
      <svg width="9" height="6" viewBox="0 0 9 6" aria-hidden="true"><path d="M1 1l3.5 3.5L8 1" fill="none" stroke="#333" stroke-width="1.2"/></svg>
    </div>
    <p class="abs shift-meta meta-job">JOB NUMBER <strong>EF23456</strong></p>
    <p class="abs shift-meta meta-category">CATAGORY CODE <strong>LRS</strong></p>
    <div class="abs btn-primary btn-clock-in">Clock In</div>
  </section>

  <section class="abs alert-card">
    <svg class="abs alert-bell" width="30" height="28" viewBox="0 0 30 28" aria-hidden="true">
      <g fill="none" stroke="#555" stroke-width="1.4" stroke-linecap="round">
        <path d="M3 6a10 10 0 014-4"/><path d="M27 6a10 10 0 00-4-4"/>
      </g>
      <path d="M15 3c-5 0-7.5 4-7.5 9v5l-3 4h21l-3-4v-5c0-5-2.5-9-7.5-9z" fill="var(--bell)" stroke="#555" stroke-width="1.2"/>
      <circle cx="15" cy="24" r="2.6" fill="var(--bell)" stroke="#555" stroke-width="1.2"/>
    </svg>
    <p class="abs alert-text">DCCHA Training expires in <span class="days">5</span> days</p>
    <span class="abs alert-close">✕</span>
  </section>

  <h2 class="abs section-title">Weekly Report</h2>
  <section class="abs report-card">
    <svg width="0" height="0" style="position:absolute" aria-hidden="true">
      <defs>
        <linearGradient id="work-grad" x1="0" y1="0" x2="0" y2="1">
          <stop offset="0" stop-color="var(--ring-blue-a)"/><stop offset="1" stop-color="var(--ring-blue-b)"/>
        </linearGradient>
      </defs>
    </svg>
    <div class="abs metric metric-work">
      <p class="metric-label">Work</p>
      <div class="metric-ring">
        <svg width="70" height="70" viewBox="0 0 70 70"><circle cx="35" cy="35" r="30" fill="none" stroke="url(#work-grad)" stroke-width="7"/></svg>
        <span>89%</span>
      </div>
      <p class="metric-hours">39hours</p>
    </div>
    <div class="abs metric metric-leave">
      <p class="metric-label">Leave</p>
      <div class="metric-ring">
        <svg width="70" height="70" viewBox="0 0 70 70">
          <circle cx="35" cy="35" r="30" fill="none" stroke="var(--ring-dark)" stroke-width="7"/>
          <circle cx="35" cy="35" r="30" fill="none" stroke="var(--ring-purple)" stroke-width="7" stroke-dasharray="66 123" transform="rotate(25 35 35)"/>
        </svg>
        <span>6%</span>
      </div>
      <p class="metric-hours">4hours</p>
    </div>
    <div class="abs metric metric-training">
      <p class="metric-label">Training time</p>
      <div class="metric-ring">
        <svg width="70" height="70" viewBox="0 0 70 70">
          <circle cx="35" cy="35" r="30" fill="none" stroke="var(--ring-dark)" stroke-width="7"/>
          <circle cx="35" cy="35" r="30" fill="none" stroke="var(--ring-cyan)" stroke-width="7" stroke-dasharray="72 117" transform="rotate(95 35 35)"/>
        </svg>
        <span>19%</span>
      </div>
      <p class="metric-hours">8hours</p>
    </div>
    <div class="abs btn-primary btn-approve">Sign and Send for approval</div>
  </section>

  <nav class="abs tab-bar">
    <div class="tab tab-active">
      <svg width="26" height="26" viewBox="0 0 26 26" aria-hidden="true"><g fill="none" stroke="var(--accent)" stroke-width="1.6" stroke-linejoin="round"><rect x="2" y="3" width="22" height="15" rx="2"/><path d="M9 23h8M13 18v5"/></g></svg>
      overview
    </div>
    <div class="tab">
      <svg width="26" height="26" viewBox="0 0 26 26" aria-hidden="true"><g fill="none" stroke="#333" stroke-width="1.6" stroke-linecap="round"><rect x="4" y="3" width="18" height="21" rx="3"/><path d="M9 1.5v3M17 1.5v3M8.5 11h9M8.5 15h9M8.5 19h9"/></g></svg>
      reports
    </div>
    <div class="tab">
      <svg width="28" height="26" viewBox="0 0 28 26" aria-hidden="true"><g fill="none" stroke="#333" stroke-width="1.6" stroke-linejoin="round"><path d="M8 2h18v13h-4v4l-4-4H8z"/><path d="M6 8H2v12h3v4l4-4h9v-2"/><path d="M12 7h10M12 10.5h8" stroke-linecap="round"/></g></svg>
      messages
    </div>
    <div class="tab">
      <svg width="26" height="26" viewBox="0 0 26 26" aria-hidden="true"><g fill="none" stroke="#333" stroke-width="1.6" stroke-linecap="round"><rect x="2.5" y="2.5" width="21" height="21" rx="7"/><circle cx="9.5" cy="10.5" r=".8" fill="#333"/><circle cx="16.5" cy="10.5" r=".8" fill="#333"/><path d="M8.5 15.5c2.5 2.6 6.5 2.6 9 0"/></g></svg>
      my profile
    </div>
  </nav>
</main>
</body>
</html>
```